Business Card Design Project

We are looking to redesign the logo, business card and stationary of one of our group companies - KESTRAL SUPPLY COMPANY LLC.

The company specialises in industrial PVC and CPVC Piping systems. It is situated in the Middle East and the focus is purely in this region.

The logo work is already completed. The file is uploaded for the reference.

We are looking for a clean minimalistic design for the business card.

regards
Ormund
Updates

Hello Everyone!

Thanks for submitting your designs. 

Yet to find the right design. Probably the below links will give you guys some more idea on what we would like.

Minimalist design with some creativity.

Ormund

http://plaincardgallery.example/inspiration/15-beautifully-minimal-business-cards

http://www.quietlayouthub.example/2011/11/14/30-minimalist-business-card-design/

http://www.firmpixelnotes.example/inspiration/minimal-business-cards/

Target Market(s)

Industrial users

Industry/Entity Type

Industrial

Requirements
Must have
• - Minimalistic design

- Back side of the card should include the manufacturer BRAVOLINE CANADA's decal. The file is upload for the reference

- Further information
Company Name:
KESTRAL SUPPLY COMPANY LLC
Address:
PO Box 9087, Sharjah Industrial Area 5, Qutrani Road
Sharjah, United Arab Emirates
Telephone:
+971-6-5018-392
Fax:
+977-6-5018-393
Email:
mail@ksc-holding.example

- FYI, Kestral Supply Company LLC is the authorised distributor for BRAVOLINE CANADA in the UAE. For further information on bravoline please visit the website www.bravoline.example

```html
<!DOCTYPE html>
<html lang="en">
<head>
<meta charset="utf-8">
<title>Kestral Supply Company LLC – Business Card</title>
<link rel="stylesheet" href="https://fonts.googleapis.com/css2?family=Arimo:wght@700&display=swap">
<style>
  :root {
    --card-bg: #f4f5f6;
    --fitting-tone: #d9dbdd;
    --fitting-light: #eceeef;
    --title-blue: #3a80c8;
    --contact-blue: #1f55a8;
    --address-grey: #6e6e6e;
    --email-blue: #3a7cc2;
    --mark-dark: #2b2f33;
  }
  html, body {
    margin: 0;
    padding: 0;
    width: 1200px;
    height: 686px;
    overflow: hidden;
    background: var(--card-bg);
  }
  .card {
    position: relative;
    width: 1200px;
    height: 686px;
    overflow: hidden;
    background: var(--card-bg);
    font-family: "Arimo", Arial, sans-serif;
    font-weight: 700;
  }
  .card__backdrop {
    position: absolute;
    inset: 0;
    background:
      radial-gradient(ellipse 340px 300px at 930px 440px, var(--fitting-tone), transparent 70%),
      radial-gradient(ellipse 330px 260px at 460px 260px, var(--fitting-tone), transparent 72%),
      radial-gradient(ellipse 260px 200px at 200px 600px, var(--fitting-tone), transparent 70%),
      linear-gradient(180deg, var(--fitting-light), var(--card-bg));
    opacity: 0.85;
  }
  .company-name {
    position: absolute;
    left: 0;
    right: 0;
    top: 28px;
    margin: 0;
    text-align: center;
    color: var(--title-blue);
    font-size: 63px;
    line-height: 80px;
    letter-spacing: 1px;
    text-shadow: 0 6px 12px rgba(0, 0, 0, 0.25);
  }
  .contact-lines {
    position: absolute;
    left: 55px;
    top: 302px;
    margin: 0;
    color: var(--contact-blue);
    font-size: 32px;
    line-height: 46px;
  }
  .address {
    position: absolute;
    right: 16px;
    top: 278px;
    margin: 0;
    font-style: normal;
    text-align: right;
    color: var(--address-grey);
    font-size: 32px;
    line-height: 45.7px;
  }
  .brand-mark {
    position: absolute;
    left: 500px;
    top: 470px;
    width: 200px;
    display: flex;
    flex-direction: column;
    align-items: center;
    gap: 10px;
  }
  .brand-mark__square {
    width: 104px;
    height: 104px;
    border-radius: 22px;
    background: var(--mark-dark);
  }
  .brand-mark__name {
    color: var(--contact-blue);
    font-size: 22px;
    letter-spacing: 1px;
  }
  .email {
    position: absolute;
    left: 0;
    right: 0;
    top: 626px;
    margin: 0;
    text-align: center;
    color: var(--email-blue);
    font-size: 34px;
    line-height: 44px;
  }
</style>
</head>
<body>
  <div class="card">
    <div class="card__backdrop" role="img" aria-label="Faint grey illustration of industrial PVC pipe fittings"></div>

    <h1 class="company-name">KESTRAL SUPPLY<br>COMPANY LLC</h1>

    <p class="contact-lines">
      Tel: +971-6-5018-392<br>
      Fax: +977-6-5018-393
    </p>

    <address class="address">
      PO Box 9087<br>
      Sharjah Industrial Area 5<br>
      Qutrani Road<br>
      Sharjah<br>
      United Arab Emirates
    </address>

    <div class="brand-mark">
      <div class="brand-mark__square"></div>
      <span class="brand-mark__name">KESTRAL</span>
    </div>

    <p class="email">Email: mail@ksc-holding.example</p>
  </div>
</body>
</html>
```